Page Design For Free Videos Download Page

We have page that already has functional code here http://www.vexarnoble.com/
The project is to create a better design and layout of that page.

You may use the password "1234" to access the features when prompted.*** Please note that the existing design is just a draft for your reference.

The page you design should have seven main components as described below:

1. Header. Include our logo and the title "Free FlickerSpans Updated Monthly"

2. Navigation. This is not yet implemented but we would like you to have these choices:

Free Videos
FlickerSpans
PebbleClips
Free Sign-Up
About Us

3. The main background image or pattern. You may incorporate our logo in some way in this background if you like (abstract, tiling, etc) but this is not required.

4. Preview Images. You can see that there are a few groups showing recent months of the free videos we will offer for download on this page. We prefer to keep the current size and functionality of the images as-is.

There will always be 16 images in rows of 4 for a clean layout. You can see from the page how these will look in rows of 4. The images will be the same size and function as the images in the example page.

5. Row text. Each row has some text showing what month the free videos belong to. The text can be displayed in any way you see fit. In the example page it is simply above each row of images but you can resize and move the text anywhere you feel is best for the design.

6. Password pop-up. If a user has not entered the password and attempts to download a video by clicking on an image, a pop-up appears asking for the password. This is only partially implemented on the test page. We want to give the user two options:

a. Please enter your password.
-or-
b. Immediately receive the password by entering your email address.

For "b" also include a checkbox: "Send me monthly updates when new free downloads become available."
also allow the user to enter their email here a

7. Banner Area. Below the image groups will be banners where we will advertise products on our website www.flickerspans.com. This is the main reason for creating this page - drive traffic to this page and then get them to sign-up to receive the password and eventually click on a banner to browse our website.

For this part you should design 4 wide template banners stacked one on top of another - each with a different layout and style but still keeping with the general theme of the page (no Flash please).

If we select you, we will give you assets (images and text) to insert into your 4 banner templates for the final files delivery. This way for now the banners can be generic.

Target Market(s)

Video professionals in the editing and live performance markets.

Industry/Entity Type

Delivery

Requirements
Must have
• 4 rows of 4 images the same size as in the example page. The image spacing and layout can change to fit your design however.

```html
<!DOCTYPE html>
<html lang="en">
<head>
<meta charset="utf-8">
<title>Free FlickerSpans</title>
<link href="https://fonts.googleapis.com/css2?family=Titillium+Web:wght@300;400;600&display=swap" rel="stylesheet">
<style>
:root{
  --bg:#060a12;
  --blue:#3d8fc0;
  --blue-bright:#4a9fd2;
  --nav-top:#3a7ea6;
  --nav-bottom:#0f2a40;
  --tab-light:#e4e6ea;
  --tab-mid:#a8adb5;
  --text-light:#eef2f6;
  --label:#8a919a;
  --rule:#2a3039;
  --thumb-border:#3a4049;
  --icon:#6a7079;
}
*{margin:0;padding:0;box-sizing:border-box}
html,body{width:1083px;height:1200px;overflow:hidden;background:var(--bg);font-family:'Titillium Web',sans-serif}
.page{position:relative;width:1083px;height:1200px;overflow:hidden;background:var(--bg)}
.header-glow{position:absolute;left:20px;top:30px;width:520px;height:150px;
  background:radial-gradient(ellipse at 40% 50%,rgba(60,140,200,.35),rgba(60,140,200,0) 65%)}
.brand{position:absolute;left:196px;top:58px;display:flex;align-items:center;gap:14px}
.brand-dot{width:42px;height:42px;border-radius:50%;background:var(--blue-bright)}
.brand-name{font-size:50px;font-weight:300;color:var(--text-light);letter-spacing:1px;line-height:1}
.tagline{position:absolute;left:340px;top:124px;font-size:16px;font-weight:600;letter-spacing:3px;color:var(--text-light)}
.nav{position:absolute;left:100px;top:169px;width:885px;height:68px;display:flex;
  background:linear-gradient(var(--nav-top),var(--nav-bottom))}
.nav-tab{width:228px;height:68px;display:flex;align-items:center;padding-left:25px;
  font-size:25px;font-weight:600;color:var(--text-light)}
.nav-tab.active{background:linear-gradient(var(--tab-light),var(--tab-mid));color:#15202c;padding-left:21px}
.sign-in{position:absolute;right:18px;top:14px;width:164px;height:44px;border-radius:3px;
  background:#4793c0;border:1px solid #6ab0da;color:var(--text-light);font-size:21px;
  display:flex;align-items:center;padding-left:48px}
.sign-in svg{position:absolute;right:16px;top:18px}
.title-band{position:absolute;left:100px;top:237px;width:885px;height:60px;
  background:linear-gradient(#6d737c,rgba(6,10,18,0))}
.page-title{position:absolute;left:118px;top:246px;font-size:56px;font-weight:400;color:var(--blue);line-height:1}
.month{position:absolute;left:100px;width:886px}
.month-rule{height:1px;background:var(--rule)}
.month-label{font-size:28px;font-weight:400;color:var(--label);margin-top:8px;line-height:1.2}
.thumbs{display:flex;gap:28px;margin-top:16px}
.thumb{position:relative;width:200px;height:188px;border:1px solid var(--thumb-border);background:#070b13}
.thumb svg{position:absolute;right:10px;bottom:10px}
.month.faded{opacity:.45}
.fade{position:absolute;left:0;top:960px;width:1083px;height:240px;
  background:linear-gradient(rgba(6,10,18,0),var(--bg) 75%)}
</style>
</head>
<body>
<div class="page">
  <div class="header-glow"></div>
  <div class="brand"><span class="brand-dot"></span><span class="brand-name">flickerspans</span></div>
  <div class="tagline">FREE FLICKERSPANS UPDATED MONTHLY</div>

  <nav class="nav">
    <div class="nav-tab">Free Videos</div>
    <div class="nav-tab active">FlickerSpans</div>
    <div class="nav-tab">PebbleClips</div>
    <div class="sign-in">Sign In
      <svg width="12" height="10" viewBox="0 0 12 10"><path d="M0 0H12L6 10Z" fill="#eef2f6"/></svg>
    </div>
  </nav>

  <div class="title-band"></div>
  <h1 class="page-title">Free FlickerSpans</h1>

  <section class="month" style="top:333px">
    <div class="month-rule"></div>
    <div class="month-label">APRIL 2013</div>
    <div class="thumbs">
      <div class="thumb"><svg width="26" height="26" viewBox="0 0 26 26"><path d="M2 10V24H24V10H20V20H6V10Z M10 2H16V11H20L13 18L6 11H10Z" fill="var(--icon)"/></svg></div>
      <div class="thumb"><svg width="34" height="38" viewBox="0 0 34 38"><path d="M32 2C22 4 14 12 10 24L14 28C26 24 32 14 32 2Z M8 22L4 22L10 14L14 14Z M16 30L16 34L24 28L24 24Z M9 27L2 36L11 29Z" fill="var(--icon)"/></svg></div>
      <div class="thumb"><svg width="26" height="26" viewBox="0 0 26 26"><path d="M2 10V24H24V10H20V20H6V10Z M10 2H16V11H20L13 18L6 11H10Z" fill="var(--icon)"/></svg></div>
      <div class="thumb"><svg width="26" height="26" viewBox="0 0 26 26"><path d="M2 10V24H24V10H20V20H6V10Z M10 2H16V11H20L13 18L6 11H10Z" fill="var(--icon)"/></svg></div>
    </div>
  </section>

  <section class="month" style="top:619px">
    <div class="month-rule"></div>
    <div class="month-label">MARCH 2013</div>
    <div class="thumbs">
      <div class="thumb"><svg width="26" height="26" viewBox="0 0 26 26"><path d="M2 10V24H24V10H20V20H6V10Z M10 2H16V11H20L13 18L6 11H10Z" fill="var(--icon)"/></svg></div>
      <div class="thumb"><svg width="26" height="26" viewBox="0 0 26 26"><path d="M2 10V24H24V10H20V20H6V10Z M10 2H16V11H20L13 18L6 11H10Z" fill="var(--icon)"/></svg></div>
      <div class="thumb"><svg width="34" height="38" viewBox="0 0 34 38"><path d="M32 2C22 4 14 12 10 24L14 28C26 24 32 14 32 2Z M8 22L4 22L10 14L14 14Z M16 30L16 34L24 28L24 24Z M9 27L2 36L11 29Z" fill="var(--icon)"/></svg></div>
      <div class="thumb"><svg width="26" height="26" viewBox="0 0 26 26"><path d="M2 10V24H24V10H20V20H6V10Z M10 2H16V11H20L13 18L6 11H10Z" fill="var(--icon)"/></svg></div>
    </div>
  </section>

  <section class="month faded" style="top:905px">
    <div class="month-rule"></div>
    <div class="month-label">FEBRUARY 2013</div>
    <div class="thumbs">
      <div class="thumb"></div>
      <div class="thumb"></div>
      <div class="thumb"></div>
      <div class="thumb"></div>
    </div>
  </section>

  <div class="fade"></div>
</div>
</body>
</html>
```